Corvale Property Website

Our organization has multiple arms. We want a 5-page website to address the divisions of our company. Pelgrave Works, our 1500 square foot flex office space will have 3 of those pages. We need a landing page for Corvale Property Enterprises and a Contact Us page for the organization. Then the 3 pages dedicated to Pelgrave Works: a page showing office pictures, a page for pricing, and a calendar page for this part of our business; for a total of 5 pages.
Updates

Please note, we need a logo for Pelgrave Works (the flex office space). We have a logo for Corvale Property (see attachments). It is not a requirement for Pelgrave's logo to match Corvale's logo.

Industry/Entity Type

Real Estate

Coding

Coded - Design and coding required

Number of Pages Required

1 page

Requirements
Must have
• Domain, Email, Logo (for Pelgrave Works),

```html
<!DOCTYPE html>
<html lang="en">
<head>
<meta charset="utf-8">
<title>Corvale Property</title>
<link rel="stylesheet" href="https://fonts.googleapis.com/css2?family=Lexend:wght@400;500;600&family=Tinos:ital,wght@0,400;0,700;1,400&family=Arimo:ital,wght@0,400;0,600;0,700;1,400&display=swap">
<style>
:root{
  --ink:#111;
  --grey:#8a8a8a;
  --line:#e6e6e6;
  --yellow:#ffc400;
  --cyan:#13b5e0;
  --teal:#1aa6d6;
  --pink:#e3226a;
  --green:#b2d42a;
  --black:#000;
  --white:#fff;
}
*{box-sizing:border-box;margin:0;padding:0}
html,body{width:1200px;height:3776px;overflow:hidden}
body{position:relative;background:var(--white);font-family:"Arimo",sans-serif;color:var(--ink)}
.abs{position:absolute}

/* top bar */
.topbar{left:444px;top:0;width:545px;height:44px;background:var(--cyan);color:var(--white);font-size:12.5px;display:flex;align-items:center;gap:28px;padding-left:32px;clip-path:polygon(0 50%,4% 0,96% 0,100% 50%,96% 100%,4% 100%)}
.topbar span{display:flex;align-items:center;gap:8px}
.login{left:1010px;top:11px;color:var(--yellow);font-family:"Lexend",sans-serif;font-size:13px;display:flex;gap:7px;align-items:center}
.header{left:0;top:0;width:1200px;height:125px;background:var(--white);z-index:2}
.nav{left:420px;top:80px;display:flex;font-size:13.5px;z-index:3}
.nav a{color:#222;text-decoration:none;position:absolute;white-space:nowrap}
.nav a.active{color:#7fb51f}
.nav a.active::after{content:"";position:absolute;left:0;right:0;top:27px;height:5px;border-radius:3px;background:#7fb51f}
.brand-disc{left:125px;top:0;width:190px;height:190px;border-radius:50%;background:var(--white);z-index:3;display:flex;flex-direction:column;align-items:center;justify-content:flex-end;padding-bottom:44px}
.brand-name{font-family:"Tinos",serif;font-size:30px;letter-spacing:5px;color:#111}
.brand-sub{font-family:"Arimo",sans-serif;font-size:7px;letter-spacing:2.4px;color:#333;margin-top:2px}

/* hero */
.hero{left:0;top:125px;width:1200px;height:783px;z-index:1}
.hero-photo{position:absolute;inset:0;background:linear-gradient(90deg,rgba(20,30,30,.55),rgba(0,0,0,0) 45%),linear-gradient(180deg,#3f5c72 0%,#7aa0b4 30%,#6b8aa0 48%,#51703d 62%,#3c5a20 80%,#2f4a18 100%);clip-path:polygon(0 0,1200px 0,1200px 666px,1021px 600px,630px 776px,151px 622px,0 659px)}
.hero-edges{position:absolute;left:0;top:0}
.hero-copy{left:111px;top:180px;color:var(--white);z-index:2}
.hero-copy .kicker{font-family:"Lexend",sans-serif;font-size:24px;color:var(--yellow);font-weight:500}
.hero-copy h1{font-family:"Tinos",serif;font-weight:700;font-size:56px;line-height:60px;letter-spacing:1px;margin-top:6px}
.hero-copy p{font-size:13.5px;line-height:25px;width:330px;margin-top:10px}
.btn{display:inline-block;background:var(--yellow);color:var(--white);font-family:"Lexend",sans-serif;font-size:15px;border-radius:26px;width:154px;height:50px;line-height:50px;text-align:center;margin-top:24px}

/* listings */
.section-title{font-family:"Tinos",serif;font-weight:700;font-size:36px;text-align:center;width:1200px;left:0;letter-spacing:.5px}
.card{width:313px;height:416px;background:var(--white);border-radius:22px;box-shadow:0 6px 16px rgba(0,0,0,.12);overflow:hidden}
.card .photo{height:227px;position:relative}
.badge{position:absolute;left:174px;top:35px;width:120px;height:28px;border-radius:14px;background:var(--yellow);color:var(--white);font-size:11.5px;font-weight:700;text-align:center;line-height:28px}
.card .body{padding:22px 21px 0}
.price{font-family:"Lexend",sans-serif;font-size:18px;font-weight:500}
.card h3{font-family:"Tinos",serif;font-weight:700;font-size:19.5px;margin-top:12px}
.loc{display:flex;align-items:center;gap:6px;color:#a0a0a0;font-size:12.5px;margin-top:14px;padding-bottom:12px;border-bottom:1px solid var(--line)}
.stats{display:flex;align-items:center;gap:18px;font-size:14px;color:#333;margin-top:14px;padding-left:8px}
.stats span{display:flex;align-items:center;gap:6px}

/* booking */
.booking{left:0;top:2007px;width:1200px;height:590px;background:linear-gradient(90deg,#9ccf1e 0%,#c3df2b 45%,#d0e436 100%)}
.booking-title{color:var(--white);top:2054px}
.calendar{left:108px;top:2124px;width:556px;height:402px;background:var(--white);border-radius:16px;padding:30px 26px 0}
.cal-head{display:flex;justify-content:space-between;font-family:"Lexend",sans-serif;font-size:19px;padding:0 10px;height:40px}
.cal-head .yr{color:var(--yellow)}
.cal-head .mo{color:#111;font-weight:500}
.cal-grid{display:grid;grid-template-columns:repeat(7,1fr);margin-top:14px;font-size:16.5px;text-align:center;row-gap:0}
.cal-grid div{height:52px;line-height:36px}
.cal-grid .dow{font-weight:700;font-size:15.5px;height:44px}
.cal-grid .today span{display:inline-block;width:36px;height:36px;border-radius:50%;background:var(--cyan);color:var(--white)}
.offer{left:683px;top:2124px;width:405px;height:402px;background:var(--white);border-radius:16px;overflow:hidden}
.offer .photo{height:201px;background:linear-gradient(180deg,#c9d6dc 0%,#e8ecee 40%,#b88a5e 75%,#8a6140 100%)}
.offer .body{padding:10px 22px 0 20px}
.offer h3{font-family:"Tinos",serif;font-weight:700;font-size:20px;padding-left:4px}
.offer .rate{color:var(--pink);font-size:15px;margin-top:9px}
.offer p{font-size:14px;line-height:25px;color:#444;margin-top:6px}
.offer a{color:var(--pink);font-size:12.5px;display:inline-block;margin-top:8px;border-bottom:1px solid var(--pink);padding:0 3px}

/* testimonials */
.quote-mark{left:574px;top:2660px;width:62px;height:62px;border-radius:50%;background:var(--yellow);color:var(--white);font-family:"Tinos",serif;font-weight:700;font-size:52px;text-align:center;line-height:76px}
.t-intro{left:0;width:1200px;top:2792px;text-align:center;font-size:13px;line-height:26px;color:#444}
.tcard{top:2883px;width:408px;height:198px;background:var(--white);box-shadow:0 6px 18px rgba(0,0,0,.06);padding:26px 24px 0}
.tcard.faded{opacity:.4}
.tcard p{font-style:italic;font-size:13px;line-height:26px;color:#555}
.person{display:flex;align-items:center;gap:12px;margin-top:14px}
.avatar{width:52px;height:52px;border-radius:50%;background:linear-gradient(180deg,#d8d8d8,#9a9a9a)}
.person .name{font-family:"Lexend",sans-serif;color:var(--cyan);font-size:17px}
.person .role{font-size:14px;color:#777;margin-top:2px}
.dots{left:583px;top:3142px;display:flex;gap:5px}
.dots i{width:10px;height:10px;border-radius:50%;background:#c9c9c9}
.dots i:first-child{background:var(--cyan)}

/* footer */
.footer{left:0;top:3230px;width:1200px;height:546px}
.footer-bg{position:absolute;left:0;top:0}
.f-brand{left:115px;top:3570px;width:210px;text-align:center;color:var(--white)}
.f-brand .brand-name{color:var(--white);font-size:36px;letter-spacing:6px}
.f-brand .brand-sub{color:var(--white);font-size:8.5px;letter-spacing:3px}
.f-col{top:3455px;color:var(--white)}
.f-col h4{font-family:"Tinos",serif;font-weight:700;font-size:21px;letter-spacing:.5px}
.f-col li{list-style:none;font-size:14px;line-height:22px}
.contact li{display:flex;gap:9px;margin-top:8px}
.contact li svg{margin-top:4px;flex:none}
.support li{margin-top:8px;padding-left:3px}
.socials{display:flex;gap:8px;margin-top:18px}
.socials i{width:30px;height:30px;border-radius:50%;background:var(--teal);border:2px solid var(--white)}
.partner{display:flex;align-items:center;gap:14px;margin-top:24px;margin-left:-14px}
.partner b{font-family:"Tinos",serif;font-weight:700;font-size:15px;letter-spacing:.5px}
.partner i{width:40px;height:40px;border-radius:50%;background:var(--cyan)}
.f-rule{left:110px;top:3674px;width:980px;height:1px;background:#2a2a2a}
.copyright{left:0;width:1200px;top:3712px;text-align:center;color:var(--white);font-size:14px}
</style>
</head>
<body>

<header class="abs header"></header>
<div class="abs topbar">
  <span><svg width="10" height="13" viewBox="0 0 10 13"><path d="M5 0a5 5 0 0 1 5 5c0 3.5-5 8-5 8S0 8.5 0 5a5 5 0 0 1 5-5z" fill="#fff"/><circle cx="5" cy="5" r="1.8" fill="#13b5e0"/></svg>12/b Corvale Property Lorem ipsum dolor sit amet,</span>
  <span><svg width="12" height="12" viewBox="0 0 12 12"><path d="M2.5 0.5l2 2.5-1.2 1.5a7 7 0 0 0 4 4L8.8 7.3l2.7 2-1 2.2C5.5 11.5.5 6.5.5 1.5z" fill="#fff"/></svg>+1 555 014 2290</span>
</div>
<div class="abs login"><svg width="11" height="12" viewBox="0 0 11 12"><circle cx="5.5" cy="3" r="3" fill="#ffc400"/><path d="M0 12c0-3.5 2.5-5 5.5-5s5.5 1.5 5.5 5z" fill="#ffc400"/></svg>Login</div>
<nav class="abs nav">
  <a class="active" style="left:0">Home</a>
  <a style="left:84px">About Us</a>
  <a style="left:188px">Services</a>
  <a style="left:288px">Buy</a>
  <a style="left:354px">Sell</a>
  <a style="left:419px">Our Team</a>
  <a style="left:524px">Blog</a>
  <a style="left:594px">Contact Us</a>
</nav>
<div class="abs brand-disc"><div class="brand-name">CORVALE</div><div class="brand-sub">PROPERTY ENTERPRISES</div></div>

<section class="abs hero">
  <div class="hero-photo" role="img" aria-label="Blue-roofed family house on a green lawn at dusk with colourful shard shapes rising behind it"></div>
  <svg class="hero-edges" width="1200" height="790" viewBox="0 0 1200 790">
    <defs>
      <linearGradient id="edgeL" x1="0" x2="1"><stop offset="0" stop-color="#e7266b"/><stop offset=".3" stop-color="#f58a1f"/><stop offset=".65" stop-color="#f7cf10"/><stop offset="1" stop-color="#19c3d8"/></linearGradient>
      <linearGradient id="edgeR" x1="0" x2="1"><stop offset="0" stop-color="#19c3e6"/><stop offset=".6" stop-color="#1d6fd0"/><stop offset="1" stop-color="#b5d42a"/></linearGradient>
    </defs>
    <polygon points="0,659 151,622 630,776 151,640 0,674" fill="url(#edgeL)"/>
    <polygon points="630,776 1021,600 1200,666 1200,682 1021,618" fill="url(#edgeR)"/>
  </svg>
</section>
<div class="abs hero-copy">
  <div class="kicker">Welcome To</div>
  <h1>CORVALE<br>PROPERTY</h1>
  <p>Lorem ipsum dolor sit amet, consectetur adipiscing elit, sed do eiusmod tempor incididunt</p>
  <span class="btn">Learn More</span>
</div>

<h2 class="abs section-title" style="top:988px">CORVALE PROPERTY GROUP</h2>

<!-- listing cards -->
<article class="abs card" style="left:110px;top:1081px">
  <div class="photo" role="img" aria-label="Bright bathroom with dark vanity and mirrors" style="background:linear-gradient(180deg,#f2f2f2,#d9d9d9 55%,#2b2b2b 56%,#3a3a3a 80%,#cfcfcf)"><span class="badge">Homes Available</span></div>
  <div class="body"><div class="price">$500,000+</div><h3>Lorem ipsum dolor sit amet</h3>
  <div class="loc"><svg width="12" height="15" viewBox="0 0 10 13"><path d="M5 0a5 5 0 0 1 5 5c0 3.5-5 8-5 8S0 8.5 0 5a5 5 0 0 1 5-5z" fill="#13b5e0"/><circle cx="5" cy="5" r="1.8" fill="#fff"/></svg>Lorem ipsum dolor sit amet</div>
  <div class="stats"><span><svg width="14" height="10" viewBox="0 0 14 10" fill="none" stroke="#999" stroke-width="1.4"><path d="M1 4V2h10M9 0l2 2-2 2M13 6v2H3M5 10 3 8l2-2"/></svg>500 Sqft</span><span><svg width="14" height="10" viewBox="0 0 14 10"><path d="M2 5l2-4h6l2 4v4H2z" fill="#999"/></svg>3</span><span><svg width="13" height="11" viewBox="0 0 13 11"><path d="M1 0v6h12v2a3 3 0 0 1-3 3H4a3 3 0 0 1-3-3" fill="#999"/></svg>4</span></div></div>
</article>
<article class="abs card" style="left:442px;top:1081px">
  <div class="photo" role="img" aria-label="Empty white room with wooden floor" style="background:linear-gradient(180deg,#f4f4f4,#e3e3e3 55%,#9b7454 70%,#6f4f36)"></div>
  <div class="body"><div class="price">$369,900+</div><h3>Lorem ipsum dolor sit amet</h3>
  <div class="loc"><svg width="12" height="15" viewBox="0 0 10 13"><path d="M5 0a5 5 0 0 1 5 5c0 3.5-5 8-5 8S0 8.5 0 5a5 5 0 0 1 5-5z" fill="#13b5e0"/><circle cx="5" cy="5" r="1.8" fill="#fff"/></svg>Lorem ipsum dolor sit amet</div>
  <div class="stats"><span><svg width="14" height="10" viewBox="0 0 14 10" fill="none" stroke="#999" stroke-width="1.4"><path d="M1 4V2h10M9 0l2 2-2 2M13 6v2H3M5 10 3 8l2-2"/></svg>500 Sqft</span><span><svg width="14" height="10" viewBox="0 0 14 10"><path d="M2 5l2-4h6l2 4v4H2z" fill="#999"/></svg>3</span><span><svg width="13" height="11" viewBox="0 0 13 11"><path d="M1 0v6h12v2a3 3 0 0 1-3 3H4a3 3 0 0 1-3-3" fill="#999"/></svg>4</span></div></div>
</article>
<article class="abs card" style="left:775px;top:1081px">
  <div class="photo" role="img" aria-label="Large suburban house with lawn under blue sky" style="background:linear-gradient(180deg,#5c8fd0,#a9c6e6 40%,#8e8a86 60%,#4f8a2e 80%,#3f7424)"></div>
  <div class="body"><div class="price">$369,900+</div><h3>Lorem ipsum dolor sit amet</h3>
  <div class="loc"><svg width="12" height="15" viewBox="0 0 10 13"><path d="M5 0a5 5 0 0 1 5 5c0 3.5-5 8-5 8S0 8.5 0 5a5 5 0 0 1 5-5z" fill="#13b5e0"/><circle cx="5" cy="5" r="1.8" fill="#fff"/></svg>Lorem ipsum dolor sit amet</div>
  <div class="stats"><span><svg width="14" height="10" viewBox="0 0 14 10" fill="none" stroke="#999" stroke-width="1.4"><path d="M1 4V2h10M9 0l2 2-2 2M13 6v2H3M5 10 3 8l2-2"/></svg>500 Sqft</span><span><svg width="14" height="10" viewBox="0 0 14 10"><path d="M2 5l2-4h6l2 4v4H2z" fill="#999"/></svg>3</span><span><svg width="13" height="11" viewBox="0 0 13 11"><path d="M1 0v6h12v2a3 3 0 0 1-3 3H4a3 3 0 0 1-3-3" fill="#999"/></svg>2</span></div></div>
</article>
<article class="abs card" style="left:110px;top:1522px">
  <div class="photo" role="img" aria-label="Dark stone house lit warmly at night" style="background:linear-gradient(180deg,#1d3358,#324a6a 40%,#5a4a38 65%,#2c3a22)"></div>
  <div class="body"><div class="price">$369,900+</div><h3>Lorem ipsum dolor sit amet</h3>
  <div class="loc"><svg width="12" height="15" viewBox="0 0 10 13"><path d="M5 0a5 5 0 0 1 5 5c0 3.5-5 8-5 8S0 8.5 0 5a5 5 0 0 1 5-5z" fill="#13b5e0"/><circle cx="5" cy="5" r="1.8" fill="#fff"/></svg>Lorem ipsum dolor sit amet</div>
  <div class="stats"><span><svg width="14" height="10" viewBox="0 0 14 10" fill="none" stroke="#999" stroke-width="1.4"><path d="M1 4V2h10M9 0l2 2-2 2M13 6v2H3M5 10 3 8l2-2"/></svg>2508&nbsp; Sqft</span><span><svg width="14" height="10" viewBox="0 0 14 10"><path d="M2 5l2-4h6l2 4v4H2z" fill="#999"/></svg>2</span><span><svg width="13" height="11" viewBox="0 0 13 11"><path d="M1 0v6h12v2a3 3 0 0 1-3 3H4a3 3 0 0 1-3-3" fill="#999"/></svg>2</span></div></div>
</article>
<article class="abs card" style="left:442px;top:1522px">
  <div class="photo" role="img" aria-label="White two-storey house with porch among trees" style="background:linear-gradient(180deg,#4f7a3a,#dfe3e2 35%,#c9cfcf 60%,#5e8d34 85%,#4a7a28)"></div>
  <div class="body"><div class="price">$369,900+</div><h3>Lorem ipsum dolor sit amet</h3>
  <div class="loc"><svg width="12" height="15" viewBox="0 0 10 13"><path d="M5 0a5 5 0 0 1 5 5c0 3.5-5 8-5 8S0 8.5 0 5a5 5 0 0 1 5-5z" fill="#13b5e0"/><circle cx="5" cy="5" r="1.8" fill="#fff"/></svg>Lorem ipsum dolor sit amet</div>
  <div class="stats"><span><svg width="14" height="10" viewBox="0 0 14 10" fill="none" stroke="#999" stroke-width="1.4"><path d="M1 4V2h10M9 0l2 2-2 2M13 6v2H3M5 10 3 8l2-2"/></svg>2508&nbsp; Sqft</span><span><svg width="14" height="10" viewBox="0 0 14 10"><path d="M2 5l2-4h6l2 4v4H2z" fill="#999"/></svg>2</span><span><svg width="13" height="11" viewBox="0 0 13 11"><path d="M1 0v6h12v2a3 3 0 0 1-3 3H4a3 3 0 0 1-3-3" fill="#999"/></svg>2</span></div></div>
</article>
<article class="abs card" style="left:775px;top:1522px">
  <div class="photo" role="img" aria-label="Modern white house with wooden panels and driveway" style="background:linear-gradient(180deg,#7ea9cf,#d8dfe4 40%,#f0f0f0 60%,#9a9690 80%,#5f8c3a)"></div>
  <div class="body"><div class="price">$369,900+</div><h3>Lorem ipsum dolor sit amet</h3>
  <div class="loc"><svg width="12" height="15" viewBox="0 0 10 13"><path d="M5 0a5 5 0 0 1 5 5c0 3.5-5 8-5 8S0 8.5 0 5a5 5 0 0 1 5-5z" fill="#13b5e0"/><circle cx="5" cy="5" r="1.8" fill="#fff"/></svg>Lorem ipsum dolor sit amet</div>
  <div class="stats"><span><svg width="14" height="10" viewBox="0 0 14 10" fill="none" stroke="#999" stroke-width="1.4"><path d="M1 4V2h10M9 0l2 2-2 2M13 6v2H3M5 10 3 8l2-2"/></svg>2508&nbsp; Sqft</span><span><svg width="14" height="10" viewBox="0 0 14 10"><path d="M2 5l2-4h6l2 4v4H2z" fill="#999"/></svg>2</span><span><svg width="13" height="11" viewBox="0 0 13 11"><path d="M1 0v6h12v2a3 3 0 0 1-3 3H4a3 3 0 0 1-3-3" fill="#999"/></svg>2</span></div></div>
</article>

<!-- booking -->
<section class="abs booking" role="img" aria-label="Green band with faded houses and colourful shard shapes"></section>
<h2 class="abs section-title booking-title">BOOKING CALENDAR</h2>
<div class="abs calendar">
  <div class="cal-head"><span class="yr">2021</span><span class="mo">Sep</span><span class="yr">2022</span></div>
  <div class="cal-grid">
    <div class="dow">Sun</div><div class="dow">Mon</div><div class="dow">Tue</div><div class="dow">Wed</div><div class="dow">Thur</div><div class="dow">Fri</div><div class="dow">Sat</div>
    <div>1</div><div>2</div><div>3</div><div>4</div><div>5</div><div class="today"><span>6</span></div><div>7</div>
    <div>8</div><div>9</div><div>10</div><div>11</div><div>12</div><div>13</div><div>14</div>
    <div>15</div><div>16</div><div>17</div><div>18</div><div>19</div><div>20</div><div>21</div>
    <div>22</div><div>23</div><div>24</div><div>25</div><div>26</div><div>29</div><div>30</div>
    <div>31</div>
  </div>
</div>
<div class="abs offer">
  <div class="photo" role="img" aria-label="Covered porch with white railings overlooking trees"></div>
  <div class="body">
    <h3>Lorem ipsum dolor sit amet</h3>
    <div class="rate">$ 1509.00</div>
    <p>Lorem ipsum dolor sit amet, consectetur adipiscing elit, sed do eiusmod tempor incididunt ut labore et dolore magna aliqua. Quis ipsum</p>
    <a>Book Now</a>
  </div>
</div>

<!-- testimonials -->
<div class="abs quote-mark">&ldquo;</div>
<h2 class="abs section-title" style="top:2736px">TESTIMONIALS</h2>
<p class="abs t-intro">Lorem ipsum dolor sit amet, consectetur adipiscing elit, sed do eiusmod tempor incididunt ut labore et<br>dolore magna aliqua. Quis ipsum suspendisse ultrices gravida.</p>

<div class="abs tcard faded" style="left:-248px"><p>Lorem ipsum dolor sit amet, consectetur adipiscing elit, sed do eiusmod tempor incididunt ut labore et dolore magna</p></div>
<div class="abs tcard" style="left:183px"><p>Lorem ipsum dolor sit amet, consectetur adipiscing elit, sed do eiusmod tempor incididunt ut labore et dolore magna aliqua. Quis ipsum suspendisse ultrices gravida.</p>
  <div class="person"><div class="avatar" role="img" aria-label="Client portrait"></div><div><div class="name">Marla Quenby</div><div class="role">Lorem Ipsum</div></div></div></div>
<div class="abs tcard" style="left:611px"><p>Lorem ipsum dolor sit amet, consectetur adipiscing elit, sed do eiusmod tempor incididunt ut labore et dolore magna aliqua. Quis ipsum suspendisse ultrices gravida.</p>
  <div class="person"><div class="avatar" role="img" aria-label="Client portrait"></div><div><div class="name">Tobin Ashcroft</div><div class="role">Lorem Ipsum</div></div></div></div>
<div class="abs tcard faded" style="left:1040px"><p>Lorem ipsum dolor sit amet, do eiusmod tempor incididunt aliqua. Quis ipsum suspendisse</p>
  <div class="person"><div class="avatar" role="img" aria-label="Client portrait"></div><div><div class="name">Renny</div><div class="role">Lorem Ipsum</div></div></div></div>
<div class="abs dots"><i></i><i></i><i></i></div>

<!-- footer -->
<footer class="abs footer">
  <svg class="footer-bg" width="1200" height="546" viewBox="0 0 1200 546">
    <defs>
      <linearGradient id="fL" x1="0" x2="1"><stop offset="0" stop-color="#e7266b"/><stop offset=".35" stop-color="#f58a1f"/><stop offset=".7" stop-color="#f7cf10"/><stop offset="1" stop-color="#19c3d8"/></linearGradient>
      <linearGradient id="fR" x1="0" x2="1"><stop offset="0" stop-color="#19c3e6"/><stop offset=".65" stop-color="#1d6fd0"/><stop offset="1" stop-color="#b5d42a"/></linearGradient>
    </defs>
    <polygon points="0,118 151,169 630,0 1021,176 1200,118 1200,546 0,546" fill="#000"/>
    <polygon points="0,108 151,156 630,0 151,169 0,118" fill="url(#fL)"/>
    <polygon points="630,0 1021,164 1200,106 1200,118 1021,176" fill="url(#fR)"/>
  </svg>
</footer>
<div class="abs f-brand"><div class="brand-name">CORVALE</div><div class="brand-sub">PROPERTY ENTERPRISES</div></div>
<div class="abs f-col contact" style="left:409px">
  <h4>CONTACT US</h4>
  <ul>
    <li style="margin-top:16px"><svg width="10" height="13" viewBox="0 0 10 13"><path d="M5 0a5 5 0 0 1 5 5c0 3.5-5 8-5 8S0 8.5 0 5a5 5 0 0 1 5-5z" fill="#fff"/><circle cx="5" cy="5" r="1.8" fill="#000"/></svg><span>432/1Corvale Property Lorem<br>ipsum dolor sit amet</span></li>
    <li><svg width="12" height="12" viewBox="0 0 12 12"><path d="M2.5 0.5l2 2.5-1.2 1.5a7 7 0 0 0 4 4L8.8 7.3l2.7 2-1 2.2C5.5 11.5.5 6.5.5 1.5z" fill="#fff"/></svg>+1 555 014 2290</li>
    <li><svg width="13" height="10" viewBox="0 0 13 10"><rect width="13" height="10" rx="1" fill="#fff"/><path d="M0 1l6.5 5L13 1" stroke="#000" fill="none"/></svg>info@corvaleproperty.com</li>
  </ul>
</div>
<div class="abs f-col support" style="left:708px">
  <h4>SUPPORT</h4>
  <ul style="margin-top:8px">
    <li>Terms &amp; Conditions</li><li>Contact us</li><li>Privacy Policy</li><li>About Us</li>
  </ul>
</div>
<div class="abs f-col" style="left:926px">
  <h4>FOLLOW US</h4>
  <div class="socials" aria-label="Social links"><i></i><i></i><i></i><i></i></div>
  <div class="partner"><i></i><b>PELGRAVE WORKS</b></div>
</div>
<div class="abs f-rule"></div>
<div class="abs copyright">©Copyrights 2022 Corvale Property&nbsp; |&nbsp;&nbsp; All Rights Reserved</div>

</body>
</html>
```